Business Card Re-Design for a Lighting Designer

I would like my business card re-designed. It is currently high gloss and they scratch too easily. I don not think the current design lends itself well to a matte finish. I have included the current design for reference along with our company logo.
Check out our website for current branding.
http://www.brambleorchidstudio.example

Updates
Some of the top contenders are muslim and it is a holiday for them. I do not want to discriminate and would expect the same courtesy for holidays we celebrate.
Target Market(s)
Interior Designers, Architects
Contact Information for Business Card
Logo - Name, Title, Address, Telephone Number and Extension, Email
Font styles to use
Requirements
Must have
- All the information listed on the current business card. If you use Red, it needs to be the red from our logo.
Nice to have
- Vertical and Horizontal Designs will be entertained.
Should not have
- Requirements for a glossy finish...should not look too corporate since we are a design firm.

```html
<!DOCTYPE html>
<html lang="en">
<head>
<meta charset="utf-8">
<title>Bramble Orchid Studio – Business Card</title>
<link rel="stylesheet" href="https://fonts.googleapis.com/css2?family=Lato:wght@300;400;700&display=swap">
<style>
  :root {
    --brand-red: #9e1b20;
    --ink: #1c1c1c;
    --grey-text: #7d7d7d;
    --grey-band: #a6a6a6;
    --paper: #ffffff;
    --backdrop: #2b2b2b;
  }
  * { margin: 0; padding: 0; box-sizing: border-box; }
  html, body {
    width: 1200px; height: 900px; overflow: hidden;
    background: var(--backdrop);
    font-family: "Lato", Arial, sans-serif;
  }
  .canvas { position: relative; width: 1200px; height: 900px; }

  .card {
    position: absolute; left: 296px; width: 607px; height: 346px;
    overflow: hidden;
  }
  .card--front { top: 85px; background: var(--paper); }
  .card--back { top: 472px; background: var(--brand-red); }

  /* front: brand block */
  .brand { position: absolute; left: 63px; top: 96px; width: 160px; }
  .brand__square {
    width: 40px; height: 40px; background: var(--brand-red); margin-bottom: 14px;
  }
  .brand__name {
    font-weight: 300; font-size: 29px; line-height: 30px; color: var(--ink);
    letter-spacing: -0.3px;
  }
  .brand__tagline {
    margin-top: 12px; font-size: 9px; letter-spacing: 1.1px; color: var(--grey-text);
  }

  .divider {
    position: absolute; left: 264px; top: 83px; width: 1.5px; height: 183px;
    background: var(--brand-red);
  }

  .contact { position: absolute; left: 313px; top: 78px; }
  .contact__name {
    font-weight: 700; font-size: 27px; line-height: 32px; color: var(--brand-red);
    letter-spacing: 0.2px;
  }
  .contact__title { font-size: 16px; color: var(--grey-text); margin-bottom: 12px; }
  .contact__address { font-size: 16px; line-height: 20px; color: var(--grey-text); margin-bottom: 10px; }
  .contact__line {
    display: flex; align-items: center; gap: 8px;
    font-size: 16px; line-height: 20px; color: var(--grey-text);
  }
  .contact__line svg { width: 10px; height: 10px; flex: none; }
  .contact__highlight { color: var(--brand-red); }

  .edge-band { position: absolute; left: 0; bottom: 0; width: 607px; height: 6px; }

  /* back */
  .back-brand { position: absolute; left: 181px; top: 88px; }
  .back-brand__name {
    font-weight: 300; font-size: 48px; line-height: 48px; color: #fff;
    letter-spacing: -0.5px;
  }
  .back-brand__rule {
    width: 238px; height: 2px; background: rgba(255,255,255,0.55); margin: 18px 0 12px;
  }
  .back-brand__tagline { font-size: 15px; letter-spacing: 2px; color: #fff; }
</style>
</head>
<body>
<main class="canvas">

  <section class="card card--front" aria-label="Business card front">
    <div class="brand">
      <div class="brand__square"></div>
      <div class="brand__name">Bramble<br>Orchid Studio</div>
      <div class="brand__tagline">LIGHTING FOR ARCHITECTURE</div>
    </div>

    <div class="divider"></div>

    <div class="contact">
      <div class="contact__name">MAREN TOLLIVER</div>
      <div class="contact__title">PRINCIPAL</div>
      <div class="contact__address">
        217 Larkspur Commons<br>Suite 410<br>Riverton, Oregon 97402
      </div>
      <div class="contact__line">
        <svg viewBox="0 0 10 10" aria-hidden="true"><path d="M2 0.5 L3.8 2.6 L2.9 3.8 Q4 6.2 6.2 7.1 L7.4 6.2 L9.5 8 L8.3 9.5 Q1.5 8.5 0.5 1.7 Z" fill="var(--brand-red)"/></svg>
        <span>555.014.2290 x1</span>
      </div>
      <div class="contact__line">
        <svg viewBox="0 0 10 10" aria-hidden="true"><rect x="0.7" y="1.8" width="8.6" height="6.4" fill="none" stroke="var(--brand-red)" stroke-width="1.2"/><path d="M0.9 2.2 L5 5.4 L9.1 2.2" fill="none" stroke="var(--brand-red)" stroke-width="1.1"/></svg>
        <span>maren@brambleorchidstudio.example</span>
      </div>
      <div class="contact__line">
        <svg viewBox="0 0 10 10" aria-hidden="true"><g fill="none" stroke="var(--brand-red)" stroke-width="0.9"><circle cx="5" cy="5" r="4.3"/><ellipse cx="5" cy="5" rx="1.9" ry="4.3"/><path d="M0.7 5 H9.3 M1.4 2.8 H8.6 M1.4 7.2 H8.6"/></g></svg>
        <span>www.<span class="contact__highlight">brambleorchidstudio</span>.example</span>
      </div>
    </div>

    <svg class="edge-band" viewBox="0 0 607 6" preserveAspectRatio="none" aria-hidden="true">
      <polygon points="0,0 304,0 294,6 0,6" fill="var(--brand-red)"/>
      <polygon points="312,0 607,0 607,6 302,6" fill="var(--grey-band)"/>
    </svg>
  </section>

  <section class="card card--back" aria-label="Business card back">
    <div class="back-brand">
      <div class="back-brand__name">Bramble<br>Orchid Studio</div>
      <div class="back-brand__rule"></div>
      <div class="back-brand__tagline">LIGHTING FOR ARCHITECTURE</div>
    </div>
  </section>

</main>
</body>
</html>
```